Residential improvers, A Quiet Harbor 9 Me *

Quiet Harbor 9 Me is a real estate company specializing in turning unloved properties into improved, happy places to live. We specialize in thoughtfully-improved residential properties for buyers or renters. Our company needs a business card that reflects the renovated homes we create using green and Feng Shui principles,

Please disregard the images we submitted. We are looking for an abstract, sophisticated elegant design. No eggs in a nest ... nothing cute. The image can be soft.
Updates

Aloha (hello) all designers. We are a serious property investment/improvement company. We strive to be unique, renovating with style and elegance. Our business card must portray the same message. We thought the nest and flower might be "it" ... clearly it's not, once we saw what you submitted. Please revisit the brief as it was modified yesterday. Mahalo for your input! We look forward to hearing from all designers that have been invited.

Industry/Entity Type

Real Estate Development

Contact Information for Business Card

We will have separate business cards for
1) Corabeth Danvers 808-555-0173 corabeth@mailtrove.net
2) Trina Vasquell 808-555-0196 trinavasquell@mailtrove.net
** can we add the website later ... in the process of approval.
Investors * Renovators * Connectors

Font styles to use
Sans Serif

Colors
cadf82

Requirements
Must have
• a feng shui feel ... modern. Color - green with black print.
Nice to have
• A Quiet Harbor 9 Me

```html
<!DOCTYPE html>
<html lang="en">
<head>
<meta charset="utf-8">
<title>Quiet Harbor 9 Me — Business Card</title>
<link href="https://fonts.googleapis.com/css2?family=Cagliostro&display=swap" rel="stylesheet">
<style>
  :root {
    --stage: #8e8f93;
    --ink: #111216;
    --ink-soft: #1d1e23;
    --green: #cadf82;
    --green-deep: #9fb068;
    --green-mid: #b7c978;
    --text-dark: #101114;
  }
  html, body {
    margin: 0;
    padding: 0;
    width: 1200px;
    height: 1200px;
    overflow: hidden;
    background: var(--stage);
  }
  .canvas {
    position: relative;
    width: 1200px;
    height: 1200px;
  }
  .card {
    position: absolute;
    left: 230px;
    width: 740px;
    height: 418px;
    background: var(--ink);
    overflow: hidden;
  }
  .card-front { top: 139px; }
  .card-back { top: 641px; }

  /* Front */
  .front-panel {
    position: absolute;
    inset: 0;
    width: 100%;
    height: 100%;
  }
  .company-name {
    position: absolute;
    right: 362px;
    top: 52px;
    margin: 0;
    font-family: "Cagliostro", sans-serif;
    font-weight: 400;
    font-size: 40px;
    line-height: 1;
    color: var(--text-dark);
    white-space: nowrap;
  }
  .contact-list {
    position: absolute;
    right: 354px;
    top: 150px;
    margin: 0;
    padding: 0;
    list-style: none;
    font-family: "Cagliostro", sans-serif;
    font-size: 20px;
    color: var(--text-dark);
    text-align: right;
  }
  .contact-list li {
    height: 40px;
    line-height: 40px;
    white-space: nowrap;
  }
  .contact-list li::after {
    content: "";
    display: inline-block;
    width: 8px;
    height: 8px;
    margin-left: 10px;
    border-radius: 50%;
    background: var(--text-dark);
    vertical-align: middle;
  }
  .stones-art {
    position: absolute;
    left: 480px;
    top: 94px;
    width: 209px;
    height: 167px;
    border-radius: 50% / 40%;
    background: radial-gradient(ellipse at 50% 60%, var(--green-mid) 0%, var(--green-deep) 55%, #2a2d22 100%);
  }

  /* Back */
  .pattern-top, .pattern-bottom {
    position: absolute;
    left: 106px;
    width: 528px;
    background: linear-gradient(90deg, var(--green-deep), var(--green), var(--green-deep));
    opacity: 0.75;
  }
  .pattern-top {
    top: -40px;
    height: 146px;
    border-radius: 0 0 140px 140px / 0 0 120px 120px;
  }
  .pattern-bottom {
    top: 282px;
    height: 136px;
    border-radius: 140px 140px 200px 200px / 60px 60px 136px 136px;
  }
  .brand-band {
    position: absolute;
    left: 0;
    top: 106px;
    width: 100%;
    height: 176px;
    background: linear-gradient(180deg, var(--ink-soft), #16171b);
    box-shadow: 0 6px 10px rgba(0,0,0,0.45);
  }
  .brand-mark {
    position: absolute;
    left: 346px;
    top: 30px;
    width: 48px;
    height: 48px;
    border-radius: 50%;
    border: 3px solid var(--green);
    box-sizing: border-box;
  }
  .brand-name {
    position: absolute;
    left: 0;
    right: 0;
    top: 112px;
    margin: 0;
    text-align: center;
    font-family: "Cagliostro", sans-serif;
    font-weight: 400;
    font-size: 44px;
    line-height: 1;
    color: var(--green);
    white-space: nowrap;
  }
</style>
</head>
<body>
<main class="canvas">
  <section class="card card-front">
    <svg class="front-panel" viewBox="0 0 740 418" aria-hidden="true">
      <defs>
        <linearGradient id="frontGreen" x1="0" y1="0" x2="1" y2="0">
          <stop offset="0" stop-color="#a0b36a"/>
          <stop offset="0.55" stop-color="#cadf82"/>
          <stop offset="1" stop-color="#a9bb6f"/>
        </linearGradient>
      </defs>
      <polygon points="0,0 482,0 370,418 0,418" fill="url(#frontGreen)"/>
    </svg>
    <h1 class="company-name">Quiet Harbor 9 Me</h1>
    <ul class="contact-list">
      <li>Corabeth Danvers</li>
      <li>808-555-0173</li>
      <li>corabeth@mailtrove.net</li>
    </ul>
    <div class="stones-art" role="img" aria-label="Stacked balance stones illustration in soft green"></div>
  </section>

  <section class="card card-back">
    <div class="pattern-top" role="img" aria-label="Green sacred geometry pattern"></div>
    <div class="pattern-bottom" role="img" aria-label="Green sacred geometry pattern"></div>
    <div class="brand-band">
      <span class="brand-mark"></span>
      <h2 class="brand-name">Quiet Harbor 9 Me</h2>
    </div>
  </section>
</main>
</body>
</html>
```